Singapore Peer-to-Peer Business Loans Site Needs a Name Card Design

We need a name card design for a new company based in Singapore called 'Ledgerbridge Capital (Singapore) Pte. Ltd.' or in short, 'LedcapSG'.
We run an online platform where small and medium enterprises can access seed capital from wealthy persons seeking high yield returns.
We need a name card design - We would like to see designs that use the colours red, black and/or grey, using any combination of the logos that we have attached. The final design should communicate transparency, innovativeness, financial savvy, and professionalism.
Target Market(s)
Sophisticated/expert financial investors and small & medium business owners.
Industry/Entity Type
Financial
Look and feel
Each slider illustrates characteristics of the customer's brand and the style your logo design should communicate.

```html
<!DOCTYPE html>
<html lang="en">
<head>
<meta charset="utf-8">
<title>LedcapSG Name Card</title>
<link rel="stylesheet" href="https://fonts.googleapis.com/css2?family=Quicksand:wght@400;700&display=swap">
<style>
  :root {
    --bg: #33434a;
    --card-white: #ffffff;
    --brand-red: #e3262b;
    --band-dark: #3a3f44;
    --panel-grey: #d2d3d5;
    --ink: #3b3e42;
    --outline: #ffffff;
  }
  * { box-sizing: border-box; margin: 0; padding: 0; }
  html, body { width: 1200px; height: 900px; overflow: hidden; }
  body {
    background: var(--bg);
    font-family: "Quicksand", sans-serif;
    display: flex;
    flex-direction: column;
    align-items: center;
    justify-content: center;
    gap: 40px;
  }
  .card {
    position: relative;
    width: 660px;
    height: 380px;
    background: var(--card-white);
    overflow: hidden;
  }
  .band {
    position: absolute;
    left: 0; right: 0; bottom: 0;
    background: var(--band-dark);
  }
  .brand-panel {
    position: absolute;
    left: -4px;
    background: var(--brand-red);
    border: 3px solid var(--outline);
    border-left: none;
    border-radius: 0 22px 22px 0;
    display: flex;
    align-items: center;
    justify-content: center;
  }
  .brand-name {
    color: #ffffff;
    font-weight: 700;
    letter-spacing: -0.5px;
  }

  /* Front */
  .card-front .band { top: 240px; }
  .card-front .brand-panel { top: 140px; width: 302px; height: 152px; }
  .card-front .brand-name { font-size: 42px; }
  .website {
    position: absolute;
    right: 36px;
    top: 252px;
    color: #ffffff;
    font-size: 21px;
    font-weight: 400;
    letter-spacing: 0.5px;
  }

  /* Back */
  .card-back .band { top: 300px; }
  .holder-name {
    position: absolute;
    left: 30px;
    top: 34px;
    font-size: 27px;
    font-weight: 400;
    color: var(--ink);
    letter-spacing: 0.5px;
  }
  .contact-panel {
    position: absolute;
    left: 175px;
    right: -4px;
    top: 133px;
    height: 190px;
    background: var(--panel-grey);
    border: 3px solid var(--outline);
    border-right: none;
    border-radius: 22px 0 0 22px;
  }
  .card-back .brand-panel { top: 156px; width: 204px; height: 204px; }
  .card-back .brand-name { font-size: 30px; }
  .contact-list {
    position: absolute;
    right: 0;
    top: 150px;
    list-style: none;
  }
  .contact-item {
    display: flex;
    align-items: center;
    justify-content: flex-end;
    gap: 12px;
    height: 36px;
    margin-bottom: 14px;
  }
  .contact-text {
    color: var(--ink);
    font-size: 17px;
    text-align: right;
    line-height: 1.4;
  }
  .contact-text.address { font-size: 16px; }
  .icon-tab {
    width: 44px;
    height: 36px;
    background: var(--brand-red);
    border: 3px solid var(--outline);
    border-right: none;
    border-radius: 8px 0 0 8px;
    display: flex;
    align-items: center;
    justify-content: center;
    flex-shrink: 0;
  }
  .icon-tab svg { width: 20px; height: 20px; }
</style>
</head>
<body>

  <section class="card card-front" aria-label="Name card front">
    <div class="band"></div>
    <div class="brand-panel"><span class="brand-name">LedcapSG</span></div>
    <span class="website">www.ledcap.sg</span>
  </section>

  <section class="card card-back" aria-label="Name card back">
    <h1 class="holder-name">Daniel Tan</h1>
    <div class="band"></div>
    <div class="contact-panel"></div>
    <div class="brand-panel"><span class="brand-name">LedcapSG</span></div>
    <ul class="contact-list">
      <li class="contact-item">
        <span class="contact-text">+65 6000 1234</span>
        <span class="icon-tab">
          <svg viewBox="0 0 24 24" aria-hidden="true"><path fill="#fff" d="M6.6 10.8a15.1 15.1 0 0 0 6.6 6.6l2.2-2.2c.3-.3.7-.4 1-.2 1.1.4 2.3.6 3.6.6.6 0 1 .4 1 1V20c0 .6-.4 1-1 1A17 17 0 0 1 3 4c0-.6.4-1 1-1h3.5c.6 0 1 .4 1 1 0 1.3.2 2.5.6 3.6.1.3 0 .7-.2 1z"/></svg>
        </span>
      </li>
      <li class="contact-item">
        <span class="contact-text">contact@ledcap.sg</span>
        <span class="icon-tab">
          <svg viewBox="0 0 24 24" aria-hidden="true"><rect x="3" y="6" width="18" height="12" rx="1" fill="none" stroke="#fff" stroke-width="1.8"/><path d="M3.5 6.5 12 13l8.5-6.5" fill="none" stroke="#fff" stroke-width="1.8"/></svg>
        </span>
      </li>
      <li class="contact-item">
        <span class="contact-text address">18 Harbour Lane, #14-00 Meridian<br>Tower, Singapore 049321</span>
        <span class="icon-tab">
          <svg viewBox="0 0 24 24" aria-hidden="true"><path d="M12 2a7 7 0 0 0-7 7c0 5 7 13 7 13s7-8 7-13a7 7 0 0 0-7-7z" fill="none" stroke="#fff" stroke-width="1.8"/><circle cx="12" cy="9" r="2.5" fill="#fff"/></svg>
        </span>
      </li>
    </ul>
  </section>

</body>
</html>
```